Venlow Vaults -responsive, bootstrap website design

Looking to build a responsive service website.

Logo and pictures have been provided.

PLEASE REVIEW ATTACHED DESIGN STYLE GUIDES & CLIENT CREATIVE BRIEF FOR OUR REQUIREMENT. THANK YOU AND GOOD LUCK!
Updates

Industry/Entity Type

Build

```html
<!DOCTYPE html>
<html lang="en">
<head>
<meta charset="utf-8">
<title>Venlow Vaults</title>
<link rel="stylesheet" href="https://fonts.googleapis.com/css2?family=Arimo:wght@400;700&display=swap">
<style>
:root{
  --topbar:#1b110d;
  --page:#2b1b15;
  --panel:#1e1310;
  --frame:#4a372c;
  --accent:#7a5538;
  --btn:#6b4a31;
  --green:#6e9a1e;
  --text:#ffffff;
  --muted:#b9aca4;
  --line:#3a2a22;
}
*{margin:0;padding:0;box-sizing:border-box}
html,body{width:896px;height:1200px;overflow:hidden}
body{position:relative;background:var(--page);font-family:"Arimo",sans-serif;color:var(--text)}
.abs{position:absolute}
.topbar{left:0;top:0;width:896px;height:29px;background:var(--topbar);font-size:8px}
.topbar span{position:absolute;top:8px}
.hero{left:0;top:29px;width:896px;height:365px;background:linear-gradient(180deg,#6f8a3a 0%,#4e6e22 35%,#5d6428 60%,#8a6a2e 85%,#6b4b22 100%)}
.bottle{left:0;top:394px;width:56px;height:806px;background:linear-gradient(90deg,#3a2a20,#2e2019)}
.sidebar{left:56px;top:29px;width:154px;height:365px;background:rgba(245,245,240,.88)}
.logo{left:92px;top:54px;width:82px;height:63px;border:1.5px solid #3a2a22;border-radius:8px;display:flex;align-items:center;justify-content:center;text-align:center;color:#2a1a12;font-size:11px;font-weight:700;line-height:1.2}
.nav a{position:absolute;left:56px;width:154px;text-align:center;font-size:13px;font-weight:700;color:#1f1410;text-decoration:none}
.nav a.active{color:var(--green)}
.nav i{position:absolute;left:56px;width:154px;height:1px;background:#c8c6c0}
.join{left:56px;top:338px;width:152px;height:36px;background:#2c241f;font-size:10px;font-weight:700;display:flex;align-items:center;justify-content:center}
.arrow{width:36px;height:36px;border-radius:50%;background:#e8e6e2;top:344px}
.panel{left:56px;top:394px;width:784px;height:716px;background:var(--panel)}
h2{position:absolute;font-size:22px;font-weight:700;color:var(--text)}
.frame{position:absolute;background:var(--frame);padding:7px}
.frame div{width:100%;height:100%}
.sub{position:absolute;font-size:12px}
.body{position:absolute;font-size:8px;line-height:14px;color:var(--muted)}
.body b{font-weight:400;color:var(--text)}
.date{left:83px;top:570px;background:rgba(75,55,40,.85);padding:4px 8px;font-size:13px;font-weight:700}
.meta{top:710px;left:76px;font-size:6.5px;color:#ddd}
.btn{left:342px;top:698px;width:74px;height:28px;background:var(--btn);font-size:10px;display:flex;align-items:center;justify-content:center}
.news h3{position:absolute;left:601px;font-size:12px;font-weight:400}
.news h3 small{font-size:10px;margin-left:10px}
.news h3 small em{font-style:normal;font-size:7px}
.sep{position:absolute;height:1px;background:var(--line)}
.retail{left:74px;top:777px;font-size:22px;font-weight:700;color:var(--accent)}
.retail-p{left:74px;top:813px;width:520px;font-size:9.5px;line-height:15px;color:#8c7b70}
.find{left:598px;top:774px;width:232px;height:69px;background:var(--btn);display:flex;align-items:center}
.find span{font-size:23px;margin-left:18px}
.thumb{top:928px;width:170px;height:133px}
.social{top:1140px;width:32px;height:32px;background:#3b2c24}
.footer{right:56px;top:1150px;font-size:8.5px;word-spacing:1px}
.footer span{margin-left:10px}
</style>
</head>
<body>
<header class="abs topbar">
  <span style="left:55px">$ - US Dollar</span>
  <span style="left:114px;top:9px;width:12px;height:8px;background:#c8ccd8"></span>
  <span style="left:130px">English</span>
  <span style="left:178px">Welcome visitor you can login or create an account.</span>
  <span style="left:639px">My Account</span>
  <span style="left:700px">Wish List (0)</span>
  <span style="left:766px">Checkout</span>
  <span style="left:820px">Login</span>
</header>

<div class="abs hero" role="img" aria-label="Photo of vineyard rows across rolling hills"></div>
<div class="abs bottle" role="img" aria-label="Dark photo of a wine bottle label"></div>
<div class="abs sidebar"></div>
<div class="abs logo">Venlow<br>Vaults</div>
<nav class="nav">
  <a class="active" style="top:142px">HOME</a><i style="top:166px"></i>
  <a style="top:178px">ABOUT</a><i style="top:202px"></i>
  <a style="top:214px">WINES</a><i style="top:238px"></i>
  <a style="top:250px">STORE</a><i style="top:274px"></i>
  <a style="top:286px">NEWS</a><i style="top:314px"></i>
</nav>
<div class="abs join">JOIN THE VENLOW FAMILY</div>
<svg class="abs arrow" style="left:801px" viewBox="0 0 36 36"><path d="M21 11l-7 7 7 7" stroke="#222" stroke-width="3" fill="none"/></svg>
<svg class="abs arrow" style="left:843px" viewBox="0 0 36 36"><path d="M15 11l7 7-7 7" stroke="#222" stroke-width="3" fill="none"/></svg>

<main class="abs panel"></main>

<section>
  <h2 style="left:76px;top:412px">BLOG</h2>
  <div class="frame" style="left:76px;top:450px;width:219px;height:156px"><div role="img" aria-label="Photo of vineyard under a pink sunset sky" style="background:linear-gradient(180deg,#7f9bc4 0%,#d99aa8 35%,#7a8a60 55%,#3f6a22 100%)"></div></div>
  <div class="abs date">22 MAY</div>
  <div class="sub" style="left:75px;top:622px">LOREM IPSUM DOLOR SIT</div>
  <p class="body" style="left:76px;top:646px;width:225px"><b>Etiam placerat suscipit mi, et tincidunt nisl blandit eu loremh</b><br>Lorem ipsum dolor sit amet, consectetur adipiscing elit. Sed blandit massa vel mauris sollicitudin dignissim. ..........</p>
  <div class="abs meta"><span style="color:var(--accent)">●</span> ADD A COMMENT &nbsp; LINK TO THIS POST &nbsp; <span style="color:var(--accent)">●</span> EMAIL A FRIEND</div>
  <div class="sep" style="left:76px;top:726px;width:222px"></div>
</section>

<section>
  <h2 style="left:339px;top:412px">ECOMMERCE</h2>
  <div class="frame" style="left:338px;top:450px;width:220px;height:156px"><div role="img" aria-label="Photo of wine glasses, grapes and bottles" style="background:linear-gradient(90deg,#5a1e14 0%,#b8863c 45%,#8a5a2a 70%,#2a1a12 100%)"></div></div>
  <div class="sub" style="left:338px;top:622px">$35/BOTTLE</div>
  <p class="body" style="left:338px;top:646px;width:225px"><b>Etiam placerat suscipit mi, et tincidunt nisl blandit eu loremh</b><br>Lorem ipsum dolor sit amet, consectetur adipiscing elit. Sed blandit massa vel mauris sollicitudin dignissim.</p>
  <div class="abs btn">VIEW MORE</div>
</section>

<section class="news">
  <h2 style="left:601px;top:412px">NEWS</h2>
  <h3 style="top:449px">NEWS FROM VENLOW VAULTS<small>2 <em>HURS</em></small></h3>
  <p class="body" style="left:601px;top:474px;width:225px"><b>Venlow Vaults releases the 2011 Maribel's Estate Cabernet</b><br>The newest vintage of our incredibly popular Cabernet Sauvignon is now available for purcha......The Venlow Family</p>
  <div class="sep" style="left:601px;top:529px;width:222px"></div>
  <h3 style="top:546px">NEWS FROM VENLOW VAULTS<small>2 <em>HURS</em></small></h3>
  <p class="body" style="left:601px;top:571px;width:225px"><b>Venlow Vaults releases the 2011 Maribel's Estate Cabernet</b><br>The newest vintage of our incredibly popular Cabernet Sauvignon is now available for purcha......The Venlow Family</p>
  <div class="sep" style="left:601px;top:626px;width:222px"></div>
  <h3 style="top:645px">NEWS FROM VENLOW VAULTS<small>2 <em>HURS</em></small></h3>
  <p class="body" style="left:601px;top:670px;width:225px"><b>Venlow Vaults releases the 2011 Maribel's Estate Cabernet</b><br>The newest vintage of our incredibly popular Cabernet Sauvignon is now available for purcha......The Venlow Family</p>
  <div class="sep" style="left:601px;top:726px;width:222px"></div>
</section>

<div class="sep" style="left:56px;top:758px;width:784px"></div>
<section>
  <div class="abs retail">RETAIL / DEALER LOCATOR</div>
  <p class="abs retail-p">PRAESENT VESTIBULUM MOLESTIE LACUS. AENEAN NONUY HENDRERIT MAURIS. PHASELLUS PORTA. FUSCE SUSCIPIT VARIUS MI.PRAESENT VESTIBULUM MOLESTIE LACUS. AENEAN NONUY HENDRERIT MAURIS.</p>
  <div class="abs find">
    <svg width="62" height="60" viewBox="0 0 62 60" style="margin-left:16px"><path d="M6 58l6-24 12 4 12-4 12 4 8 20-14-4-12 4-12-4z" fill="#fff"/><path d="M24 38v18M36 34v18" stroke="#6b4a31" stroke-width="2"/><circle cx="30" cy="14" r="9" fill="#fff"/><circle cx="30" cy="14" r="4" fill="#6b4a31"/><path d="M22 18l8 14 8-14z" fill="#fff"/></svg>
    <span>FIND HERE</span>
  </div>
</section>
<div class="sep" style="left:56px;top:856px;width:784px"></div>

<section>
  <h2 style="left:76px;top:885px">PHOTO / VIDEO GALLERY</h2>
  <div class="frame thumb" style="left:83px"><div role="img" aria-label="Photo of hazy vineyard landscape" style="background:linear-gradient(180deg,#f2efe6 0%,#d8d2bc 50%,#556a2a 75%,#3e5420 100%)"></div></div>
  <div class="frame thumb" style="left:268px"><div role="img" aria-label="Photo of dirt path between vine rows under blue sky" style="background:linear-gradient(180deg,#4a7ac4 0%,#c9d8ea 35%,#3f6e22 65%,#b8a98c 100%)"></div></div>
  <div class="frame thumb" style="left:455px"><div role="img" aria-label="Video still of dark grape clusters" style="background:linear-gradient(180deg,#2c3a1a,#1f2614)"></div></div>
  <svg class="abs" style="left:516px;top:971px" width="48" height="48" viewBox="0 0 48 48"><circle cx="24" cy="24" r="22" fill="rgba(0,0,0,.4)" stroke="#fff" stroke-width="2"/><path d="M19 15l14 9-14 9z" fill="#fff"/></svg>
  <div class="frame thumb" style="left:644px"><div role="img" aria-label="Photo of vineyard under a pink sunset sky" style="background:linear-gradient(180deg,#7f9bc4 0%,#d99aa8 35%,#4a7a26 60%,#2f5a1a 100%)"></div></div>
</section>

<footer>
  <div class="abs social" style="left:55px" role="img" aria-label="Social profile link"></div>
  <div class="abs social" style="left:98px" role="img" aria-label="Social profile link"></div>
  <div class="abs social" style="left:142px" role="img" aria-label="Social profile link"></div>
  <div class="abs footer"><span>VENLOW VAULTS</span><span>RIDGEFORD HOLLOW, OREGON</span><span>©2014. ALL RIGHTS RESERVED.</span><span>CONTACT US</span></div>
</footer>
</body>
</html>
```